Product Label Design

Need a product design for our Epsom salt product, needs to have a luxurious simple feel to it. The picture attached is our brand and wordage on it, the bag we think should be a stand up bag that should be offwhite/creme color. The other picture are products that we like. We updated the packaging to be a Kraft tube box, please see the attached photo for dimensions.

```html
<!DOCTYPE html>
<html lang="en">
<head>
<meta charset="utf-8">
<title>Luma Elevate Epsom Salt Label</title>
<link rel="stylesheet" href="https://fonts.googleapis.com/css2?family=Cormorant+Garamond:wght@400&family=Josefin+Sans:wght@200;300&display=swap">
<style>
  :root {
    --pouch-cream: #f7f4ef;
    --ink-grey: #8d8a92;
    --seal-line: #e9e5df;
    --tone-pink: #f1d3d9;
    --tone-lilac: #ddd2ec;
    --tone-blue: #d6e6ee;
  }
  * { margin: 0; padding: 0; box-sizing: border-box; }
  html, body {
    width: 800px;
    height: 1200px;
    overflow: hidden;
    background: var(--pouch-cream);
  }
  .pouch-face {
    position: relative;
    width: 800px;
    height: 1200px;
    background: var(--pouch-cream);
    overflow: hidden;
  }
  .zip-seal {
    position: absolute;
    left: 0;
    right: 0;
    top: 168px;
    height: 4px;
    border-top: 1px solid var(--seal-line);
    border-bottom: 1px solid var(--seal-line);
  }
  .tear-notch {
    position: absolute;
    top: 70px;
    width: 14px;
    height: 2px;
    background: var(--seal-line);
  }
  .tear-notch.left { left: 0; }
  .tear-notch.right { right: 0; }
  .art-area {
    position: absolute;
    left: 0;
    right: 0;
    top: 330px;
    height: 730px;
    background: linear-gradient(180deg,
      var(--pouch-cream) 0%,
      var(--tone-pink) 22%,
      var(--tone-lilac) 55%,
      var(--tone-blue) 80%,
      var(--pouch-cream) 100%);
  }
  .label-text {
    position: absolute;
    left: 0;
    right: 0;
    text-align: center;
    color: var(--ink-grey);
    line-height: 1;
  }
  .brand-name {
    top: 241px;
    font-family: "Cormorant Garamond", serif;
    font-weight: 400;
    font-size: 38px;
    letter-spacing: 6px;
  }
  .product-name {
    top: 523px;
    font-family: "Josefin Sans", sans-serif;
    font-weight: 200;
    font-size: 84px;
    letter-spacing: 6px;
  }
  .scent-line {
    top: 603px;
    font-family: "Josefin Sans", sans-serif;
    font-weight: 300;
    font-size: 23px;
    letter-spacing: 4px;
  }
  .product-type {
    top: 640px;
    font-family: "Josefin Sans", sans-serif;
    font-weight: 300;
    font-size: 23px;
    letter-spacing: 4px;
  }
  .net-weight {
    top: 984px;
    font-family: "Josefin Sans", sans-serif;
    font-weight: 300;
    font-size: 18px;
    letter-spacing: 3px;
  }
</style>
</head>
<body>
  <main class="pouch-face">
    <div class="tear-notch left"></div>
    <div class="tear-notch right"></div>
    <div class="zip-seal"></div>
    <div class="art-area" role="img" aria-label="Soft watercolour landscape in pink, lavender and pale blue"></div>
    <p class="label-text brand-name">LUMA</p>
    <h1 class="label-text product-name">ELEVATE</h1>
    <p class="label-text scent-line">LAVENDER + BERGAMOT</p>
    <p class="label-text product-type">EPSOM SALT</p>
    <p class="label-text net-weight">1.5 LB / 680 g</p>
  </main>
</body>
</html>
```